Business Card Design Project

we need a business card design for our company: www.dravonix.ch
It's important to include our already existing logo (see website)

```html
<!DOCTYPE html>
<html lang="en">
<head>
<meta charset="utf-8">
<title>Dravonix – Business Card</title>
<link href="https://fonts.googleapis.com/css2?family=Barlow:wght@400;500;600;700&display=swap" rel="stylesheet">
<style>
  :root {
    --brand-blue: #0277c6;
    --brand-navy: #0a4f8f;
    --soft-blue: #6f9fd8;
    --band-light: #8fb3e0;
    --rule-blue: #9cbde6;
    --paper: #ffffff;
    --ink: #111111;
  }
  html, body {
    margin: 0;
    padding: 0;
    width: 1200px;
    height: 900px;
    overflow: hidden;
    background: var(--paper);
    font-family: "Barlow", Arial, sans-serif;
  }
  .sheet {
    position: relative;
    width: 1200px;
    height: 900px;
  }
  .card {
    position: absolute;
    top: 252px;
    width: 550px;
    height: 329px;
    border-radius: 22px;
    overflow: hidden;
    box-shadow: 0 2px 6px rgba(0,0,0,0.35);
  }
  .card--front {
    left: 33px;
    background: var(--brand-blue);
  }
  .card--back {
    left: 609px;
    background: var(--paper);
  }
  .wordmark {
    font-weight: 700;
    letter-spacing: -0.5px;
    line-height: 1;
    margin: 0;
  }
  .card--front .wordmark {
    position: absolute;
    left: 0;
    right: 0;
    top: 130px;
    text-align: center;
    font-size: 70px;
    color: var(--paper);
  }
  .card--back .wordmark {
    position: absolute;
    left: 22px;
    top: 36px;
    font-size: 60px;
    color: var(--brand-blue);
  }
  .address {
    position: absolute;
    right: 47px;
    top: 56px;
    text-align: right;
    font-size: 16px;
    font-weight: 600;
    line-height: 19px;
    color: var(--brand-navy);
    margin: 0;
    font-style: normal;
  }
  .divider {
    position: absolute;
    left: 22px;
    right: 47px;
    top: 123px;
    height: 0;
    border-top: 1.5px solid var(--rule-blue);
  }
  .edge-band {
    position: absolute;
    right: 0;
    top: 0;
    width: 22px;
    height: 100%;
    background: var(--brand-blue);
  }
  .edge-band__accent {
    position: absolute;
    left: 0;
    top: 175px;
    width: 100%;
    height: 95px;
    background: var(--band-light);
  }
  .contacts {
    position: absolute;
    right: 47px;
    top: 193px;
    margin: 0;
    padding: 0;
    list-style: none;
  }
  .contacts li {
    display: flex;
    align-items: center;
    justify-content: flex-end;
    height: 31px;
    font-size: 16px;
    color: var(--soft-blue);
  }
  .contacts .tag {
    display: inline-flex;
    align-items: center;
    justify-content: center;
    width: 17px;
    height: 17px;
    margin-left: 18px;
    border-radius: 3px;
    background: var(--brand-blue);
    color: var(--paper);
    font-size: 11px;
    font-weight: 600;
  }
  .caption {
    position: absolute;
    top: 620px;
    width: 200px;
    text-align: center;
    font-size: 17px;
    color: var(--ink);
    letter-spacing: 0.3px;
  }
  .caption--front { left: 207px; }
  .caption--back { left: 785px; }
</style>
</head>
<body>
<main class="sheet">
  <section class="card card--front" aria-label="Card front">
    <p class="wordmark">Dravonix</p>
  </section>

  <section class="card card--back" aria-label="Card back">
    <p class="wordmark">Dravonix</p>
    <address class="address">Lindenweg 12<br>8005 Zürich</address>
    <div class="divider"></div>
    <ul class="contacts">
      <li>www.dravonix.ch<span class="tag">W</span></li>
      <li>+41 44 210 47 60<span class="tag">T</span></li>
      <li>info@dravonix.ch<span class="tag">E</span></li>
      <li>dravonix.ch<span class="tag">S</span></li>
    </ul>
    <div class="edge-band"><div class="edge-band__accent"></div></div>
  </section>

  <div class="caption caption--front">FRONT</div>
  <div class="caption caption--back">BACK</div>
</main>
</body>
</html>
```